Animal Eye Clinic needs a Business card

We are a new veterinary ophthalmology practice (Tessaly Animal Eye Care) and we need a business card designed. We only see animal eyes - we are not a regular veterinary clinic. We already have a logo. We are looking for a professional, good looking business card to hand out to our clients. We are looking for something simple but professional and contemporary. Our logo is likely the only picture/graphic that needs to be on the card.
Updates

Contact Information for Business Card

Marisol Dunkley, BSc, DVM, MSc, DipACVO
Veterinary Ophthalmologist

Phone: 250.418.3097
Email: tessalyanimaleyecare@mailbrook.net
Website: tessalyanimaleyecare.net
Address: 1840 Pellworth Rd
Kelowna, BC, V4T 8M3

Colors

Designer to choose colors to be used in the design.

Requirements
Must have
• Our logo (attached)

```html
<!DOCTYPE html>
<html lang="en">
<head>
<meta charset="utf-8">
<title>Tessaly Animal Eye Care – Business Card</title>
<link rel="stylesheet" href="https://fonts.googleapis.com/css2?family=Roboto:wght@400;500;700&display=swap">
<style>
  :root {
    --backdrop: #8c7357;
    --card-white: #f8f8f8;
    --teal: #1a97a6;
    --grey: #7a7a7b;
    --ink: #333333;
    --white: #ffffff;
  }
  * { margin: 0; padding: 0; box-sizing: border-box; }
  html, body {
    width: 900px;
    height: 1200px;
    overflow: hidden;
    background: var(--backdrop);
    font-family: "Roboto", Arial, sans-serif;
  }
  .canvas {
    position: relative;
    width: 900px;
    height: 1200px;
  }
  .card {
    position: absolute;
    left: 75px;
    width: 768px;
    height: 437px;
    border-radius: 18px;
    overflow: hidden;
    box-shadow: 0 4px 12px rgba(0,0,0,0.35);
  }
  .card-front {
    top: 133px;
    background: var(--card-white);
    text-align: center;
    color: var(--ink);
  }
  .holder-name {
    position: absolute;
    top: 64px;
    width: 100%;
    font-size: 24px;
    font-weight: 500;
    color: var(--teal);
  }
  .holder-title {
    position: absolute;
    top: 96px;
    width: 100%;
    font-size: 22px;
    font-weight: 400;
  }
  .brand {
    position: absolute;
    top: 170px;
    left: 0;
    width: 100%;
    display: flex;
    align-items: center;
    justify-content: center;
    gap: 22px;
  }
  .brand-dot {
    width: 70px;
    height: 70px;
    border-radius: 50%;
    background: var(--teal);
  }
  .brand-name {
    font-size: 38px;
    font-weight: 700;
    line-height: 1.1;
    color: var(--teal);
    text-align: left;
    text-transform: uppercase;
  }
  .contact {
    position: absolute;
    top: 296px;
    width: 100%;
    list-style: none;
    font-size: 21px;
    line-height: 30px;
  }
  .card-back {
    top: 628px;
    background: linear-gradient(to bottom, var(--teal) 0, var(--teal) 217px, var(--grey) 217px, var(--grey) 100%);
  }
  .website {
    position: absolute;
    top: 200px;
    width: 100%;
    text-align: center;
    font-size: 24px;
    font-weight: 700;
    letter-spacing: 0.5px;
    color: var(--white);
  }
</style>
</head>
<body>
<main class="canvas">
  <section class="card card-front">
    <p class="holder-name">Marisol Dunkley, BSc, DVM, MSc, DipACVO</p>
    <p class="holder-title">Veterinary Ophthalmologist</p>
    <div class="brand">
      <span class="brand-dot" aria-hidden="true"></span>
      <p class="brand-name">Tessaly<br>Animal Eye Care</p>
    </div>
    <ul class="contact">
      <li>250.418.3097</li>
      <li>tessalyanimaleyecare@mailbrook.net</li>
      <li>1840 Pellworth Rd, Kelowna, BC, V4T 8M3</li>
    </ul>
  </section>
  <section class="card card-back">
    <p class="website">WWW.TESSALYANIMALEYECARE.NET</p>
  </section>
</main>
</body>
</html>
```